Jewelers Website

This is for the DESIGN ONLY.
I am a software programmer and will be doing the development.
New website design for
www.lunagemcraft.com.au
Need a fresh new look for an online only jewellery business who produce their jewellery by hand. I would like it designed in a parallax style. Feel free to recommend fonts to use for the site. This is an Australian based company located in NSW so shots of sites in NSW might make nice background images.
http://plaxorin.me/demo/#theme=parallax
To contain the below sections
About Us
Contact Us
Gallery
Testimonials
Diamond Types
The colour scheme is to be Black / White and Silver.
With the Parallax style there will be moving sections and images for added impact.
Target Market(s)
Young Adults mainly engagement jewellery

```html
<!DOCTYPE html>
<html lang="en">
<head>
<meta charset="utf-8">
<title>Luna Gemcraft</title>
<link rel="stylesheet" href="https://fonts.googleapis.com/css2?family=Alegreya:wght@400;500&family=Alegreya+SC:wght@400;500&display=swap">
<style>
  :root {
    --ink: #ffffff;
    --ink-soft: #d9d9d9;
    --ink-dark: #111111;
    --header-bg: #2e2e2e;
    --header-line: #4a4a4a;
    --tab-top: #3b3b3b;
    --tab-bottom: #1c1c1c;
    --phone-bg: #0e0e0e;
    --footer-top: #262626;
    --footer-bottom: #0c0c0c;
    --rule: #555555;
    --rule-light: #9a9a9a;
  }
  * { box-sizing: border-box; margin: 0; padding: 0; }
  html, body { width: 1200px; height: 1044px; overflow: hidden; background: #000; }
  body { font-family: "Alegreya", Georgia, serif; color: var(--ink); }
  .page { position: relative; width: 1200px; height: 1044px; overflow: hidden; }

  /* header */
  .site-header {
    position: absolute; left: 0; top: 0; width: 1200px; height: 105px;
    background: linear-gradient(#363636, var(--header-bg));
    border-bottom: 1px solid var(--header-line);
  }
  .brand-tab {
    position: absolute; left: 88px; top: 22px; width: 298px; height: 100px; z-index: 3;
    background: linear-gradient(var(--tab-top), var(--tab-bottom));
    clip-path: polygon(0 0, 100% 0, 90% 100%, 10% 100%);
    display: flex; align-items: center; justify-content: center;
  }
  .brand-name {
    font-family: "Alegreya", Georgia, serif; font-weight: 400;
    font-size: 30px; line-height: 27px; letter-spacing: 2px; text-align: center; color: var(--ink);
    text-transform: uppercase;
  }
  .phone-bar {
    position: absolute; left: 683px; top: 7px; width: 401px; height: 33px;
    background: var(--phone-bg); display: flex; align-items: center; padding-left: 4px; gap: 2px;
  }
  .phone-number { font-size: 21px; font-weight: 500; }
  .phone-hours { font-size: 12.5px; margin-left: 6px; }
  .main-nav {
    position: absolute; left: 372px; top: 59px; height: 33px; display: flex;
    background: linear-gradient(#3a3a3a, #262626);
  }
  .main-nav a {
    display: block; height: 33px; line-height: 33px; padding: 0 19px; font-size: 15px;
    color: var(--ink); text-decoration: none; text-transform: uppercase;
    border-left: 1px solid #4c4c4c;
  }
  .main-nav a:first-child { border-left: 0; padding-left: 99px; }
  .main-nav a:last-child { padding-right: 18px; }

  /* tiles */
  .tile { position: absolute; overflow: hidden; }
  .tile .photo { position: absolute; inset: 0; }
  .tile-copy { position: absolute; text-align: center; }
  .tile-copy h2 { font-weight: 400; font-size: 28px; letter-spacing: 0.5px; text-transform: uppercase; line-height: 32px; }
  .tile-copy p { font-size: 13px; line-height: 15px; margin-top: 6px; }
  .tile-copy .rule { height: 1px; margin: 12px 0 10px; }
  .find-link { font-size: 17px; font-weight: 500; text-decoration: underline; color: inherit; text-transform: uppercase; }
  .on-dark .rule { background: var(--rule); }
  .on-light { color: var(--ink-dark); }
  .on-light .rule { background: var(--rule-light); }

  .hero-ring { left: 0; top: 105px; width: 531px; height: 365px; background: #000; }
  .hero-ring .photo {
    background:
      radial-gradient(ellipse 95px 80px at 262px 235px, rgba(215,215,215,.9) 0%, rgba(120,120,120,.55) 55%, rgba(0,0,0,0) 100%),
      radial-gradient(ellipse 60px 30px at 262px 320px, rgba(90,90,90,.5) 0%, rgba(0,0,0,0) 100%),
      radial-gradient(ellipse 190px 230px at 470px 175px, #f2f2f2 0%, #c9c9c9 35%, #8a8a8a 62%, rgba(30,30,30,0) 100%),
      linear-gradient(90deg, #000 0%, #0b0b0b 60%, #1a1a1a 100%);
  }
  .hero-ring .tile-copy { left: 69px; top: 48px; width: 262px; text-align: left; }
  .hero-ring h2 { padding-left: 19px; }
  .hero-ring .rule { margin: 24px 0 20px; }

  .hero-sets { left: 531px; top: 105px; width: 669px; height: 365px; }
  .hero-sets .photo {
    background:
      radial-gradient(ellipse 150px 90px at 340px 60px, rgba(25,25,25,.85) 0%, rgba(25,25,25,0) 100%),
      radial-gradient(ellipse 170px 170px at 420px 190px, #c9c9c9 0%, #a5a5a5 40%, rgba(120,120,120,0) 100%),
      radial-gradient(ellipse 120px 80px at 405px 330px, #e4e4e4 0%, rgba(180,180,180,0) 100%),
      radial-gradient(ellipse 200px 260px at 640px 120px, #1e1e1e 0%, rgba(30,30,30,0) 100%),
      linear-gradient(90deg, #606060 0%, #7a7a7a 40%, #8e8e8e 62%, #4a4a4a 100%);
  }
  .hero-sets .tile-copy { left: 18px; top: 122px; width: 262px; text-align: left; }
  .hero-sets h2 { padding-left: 13px; }
  .hero-sets .rule { margin: 18px 0 16px; }
  .hero-sets .find-link { display: block; text-align: center; }

  .choose-any { left: 0; top: 470px; width: 531px; height: 147px; background: #eef2f6; }
  .choose-any .photo {
    background:
      radial-gradient(ellipse 50px 45px at 205px 65px, #8c96a0 0%, rgba(140,150,160,0) 100%),
      radial-gradient(ellipse 50px 45px at 160px 120px, #7d8792 0%, rgba(125,135,146,0) 100%),
      radial-gradient(ellipse 40px 35px at 60px 100px, #a1aab3 0%, rgba(161,170,179,0) 100%),
      radial-gradient(ellipse 30px 25px at 110px 40px, #a9b2ba 0%, rgba(169,178,186,0) 100%),
      radial-gradient(ellipse 35px 30px at 250px 115px, #9aa3ac 0%, rgba(154,163,172,0) 100%),
      linear-gradient(90deg, #d6dde4 0%, #e8edf2 45%, #f4f7fa 60%, #f4f7fa 100%);
  }
  .choose-any .tile-copy { left: 293px; top: 18px; width: 228px; }

  .rings { left: 0; top: 617px; width: 531px; height: 147px; background: #000; }
  .rings .photo {
    background:
      radial-gradient(ellipse 140px 70px at 410px 50px, rgba(110,110,110,.75) 0%, rgba(40,40,40,.4) 55%, rgba(0,0,0,0) 100%),
      radial-gradient(ellipse 60px 40px at 470px 110px, rgba(90,90,90,.6) 0%, rgba(0,0,0,0) 100%),
      #000;
  }
  .rings .tile-copy { left: 31px; top: 16px; width: 230px; }

  .bracelets { left: 531px; top: 470px; width: 335px; height: 294px; background: #fff; }
  .bracelets .photo {
    background:
      radial-gradient(ellipse 60px 190px at 300px 200px, #9b9b9b 0%, #c9c9c9 45%, rgba(255,255,255,0) 100%),
      radial-gradient(ellipse 150px 110px at 90px 210px, rgba(200,200,200,.55) 0%, rgba(255,255,255,0) 100%),
      #fff;
  }
  .bracelets .tile-copy { left: 50px; top: 18px; width: 225px; }

  .earrings { left: 866px; top: 470px; width: 334px; height: 294px; }
  .earrings .photo {
    background:
      radial-gradient(ellipse 120px 100px at 200px 220px, #e6e6e6 0%, #8c8c8c 55%, rgba(140,140,140,0) 100%),
      radial-gradient(ellipse 45px 40px at 100px 160px, #dcdcdc 0%, rgba(200,200,200,0) 100%),
      radial-gradient(ellipse 40px 40px at 320px 160px, #d4d4d4 0%, rgba(200,200,200,0) 100%),
      linear-gradient(#a2a2a2 0%, #c4c4c4 45%, #a9a9a9 80%, #bdbdbd 100%);
  }
  .earrings .tile-copy { left: 63px; top: 18px; width: 224px; }

  /* footer */
  .site-footer {
    position: absolute; left: 0; top: 764px; width: 1200px; height: 280px;
    background: linear-gradient(var(--footer-top), var(--footer-bottom));
    border-top: 1px solid #3a3a3a;
  }
  .footer-rule { position: absolute; left: 121px; width: 968px; height: 1px; background: var(--rule); }
  .footer-col { position: absolute; top: 40px; }
  .footer-col h3 { font-family: "Alegreya", Georgia, serif; font-weight: 500; font-size: 17px; text-transform: uppercase; }
  .footer-list { list-style: none; margin-top: 28px; }
  .footer-list li {
    font-family: "Alegreya SC", Georgia, serif; font-size: 14px; color: var(--ink-soft);
    height: 26px; display: flex; align-items: center; gap: 14px;
  }
  .footer-note {
    font-family: "Alegreya SC", Georgia, serif; font-size: 11.5px; line-height: 16px;
    color: var(--ink-soft); text-transform: uppercase; width: 212px;
  }
  .quote-open { font-size: 16px; color: #888; position: absolute; left: 2px; top: 42px; }
  .signature-row {
    display: flex; justify-content: space-between; align-items: baseline;
    width: 230px; margin: 18px 0 0 13px;
  }
  .signature { font-family: "Alegreya SC", Georgia, serif; font-size: 13px; color: var(--ink-soft); }
  .quote-close { font-size: 15px; color: #888; }
  .copyright {
    position: absolute; left: 0; width: 1200px; top: 1016px; text-align: center;
    font-family: Arial, Helvetica, sans-serif; font-size: 10.5px; color: var(--ink-soft);
  }
</style>
</head>
<body>
<div class="page">

  <header class="site-header">
    <div class="brand-tab"><span class="brand-name">Luna<br>Gemcraft</span></div>
    <div class="phone-bar">
      <svg width="22" height="20" viewBox="0 0 22 20" aria-hidden="true">
        <path d="M2 7c0-3 4-5 9-5s9 2 9 5l-4 1-1-2c-2-1-6-1-8 0L6 8z" fill="#fff"/>
        <rect x="5" y="9" width="12" height="9" rx="2" fill="#fff"/>
        <circle cx="11" cy="13.5" r="2" fill="#0e0e0e"/>
      </svg>
      <span class="phone-number">:+61 (0)2 9000 4821</span>
      <span class="phone-hours">HOURS: 6AM-4PM PST M-FRI</span>
    </div>
    <nav class="main-nav">
      <a href="#about">About Us</a>
      <a href="#contact">Contact Us</a>
      <a href="#gallery">Gallery</a>
      <a href="#testimonials">Testimonials</a>
      <a href="#types">Diamond Types</a>
    </nav>
  </header>

  <section class="tile hero-ring on-dark">
    <div class="photo" role="img" aria-label="Close-up of a radiant-cut diamond ring with pavé halo, and a smaller full view of the ring"></div>
    <div class="tile-copy">
      <h2>Diamond Ring</h2>
      <p>Lorem Ipsum is simply dummy text of the printing and typesetting industry. Lorem</p>
      <div class="rule"></div>
      <a class="find-link" href="#">Find Now!</a>
    </div>
  </section>

  <section class="tile hero-sets on-dark">
    <div class="photo" role="img" aria-label="Black and white portrait of a model wearing a diamond necklace and drop earrings"></div>
    <div class="tile-copy">
      <h2>Jewelery Sets</h2>
      <p>Lorem Ipsum is simply dummy text of the printing and typesetting industry. Lorem</p>
      <div class="rule"></div>
      <a class="find-link" href="#">Find Now!</a>
    </div>
  </section>

  <section class="tile choose-any on-light">
    <div class="photo" role="img" aria-label="Loose cut diamonds scattered on a pale surface"></div>
    <div class="tile-copy">
      <h2>Choose Any</h2>
      <p>Lorem Ipsum is simply dummy text of the printing and typesetting industry. Lorem</p>
      <div class="rule"></div>
      <a class="find-link" href="#">Find Now!</a>
    </div>
  </section>

  <section class="tile rings on-dark">
    <div class="photo" role="img" aria-label="Sparkling diamonds falling on a black background"></div>
    <div class="tile-copy">
      <h2>Rings</h2>
      <p>Lorem Ipsum is simply dummy text of the printing and typesetting industry. Lorem</p>
      <div class="rule"></div>
      <a class="find-link" href="#">Find Now!</a>
    </div>
  </section>

  <section class="tile bracelets on-light">
    <div class="photo" role="img" aria-label="Silver diamond tennis bracelet on white"></div>
    <div class="tile-copy">
      <h2>Bracelets</h2>
      <p>Lorem Ipsum is simply dummy text of the printing and typesetting industry. Lorem</p>
      <div class="rule"></div>
      <a class="find-link" href="#">Find Now!</a>
    </div>
  </section>

  <section class="tile earrings on-light">
    <div class="photo" role="img" aria-label="Large brilliant-cut diamonds on a grey surface"></div>
    <div class="tile-copy">
      <h2>Earrings</h2>
      <p>Lorem Ipsum is simply dummy text of the printing and typesetting industry. Lorem</p>
      <div class="rule"></div>
      <a class="find-link" href="#">Find Now!</a>
    </div>
  </section>

  <footer class="site-footer">
    <div class="footer-rule" style="top:69px"></div>
    <div class="footer-rule" style="top:235px"></div>

    <div class="footer-col" style="left:121px">
      <h3>Categories</h3>
      <ul class="footer-list">
        <li><svg width="12" height="12" viewBox="0 0 12 12" aria-hidden="true"><path d="M6 0L7 5 12 6 7 7 6 12 5 7 0 6 5 5z" fill="#ccc"/></svg>Bracelets</li>
        <li><svg width="12" height="12" viewBox="0 0 12 12" aria-hidden="true"><path d="M6 0L7 5 12 6 7 7 6 12 5 7 0 6 5 5z" fill="#ccc"/></svg>Necklaces</li>
        <li><svg width="12" height="12" viewBox="0 0 12 12" aria-hidden="true"><path d="M6 0L7 5 12 6 7 7 6 12 5 7 0 6 5 5z" fill="#ccc"/></svg>Rings</li>
        <li><svg width="12" height="12" viewBox="0 0 12 12" aria-hidden="true"><path d="M6 0L7 5 12 6 7 7 6 12 5 7 0 6 5 5z" fill="#ccc"/></svg>Watches</li>
      </ul>
    </div>

    <div class="footer-col" style="left:366px">
      <h3>Information</h3>
      <ul class="footer-list">
        <li><svg width="12" height="12" viewBox="0 0 12 12" aria-hidden="true"><path d="M6 0L7 5 12 6 7 7 6 12 5 7 0 6 5 5z" fill="#ccc"/></svg>About Us</li>
        <li><svg width="12" height="12" viewBox="0 0 12 12" aria-hidden="true"><path d="M6 0L7 5 12 6 7 7 6 12 5 7 0 6 5 5z" fill="#ccc"/></svg>Delivery</li>
        <li><svg width="12" height="12" viewBox="0 0 12 12" aria-hidden="true"><path d="M6 0L7 5 12 6 7 7 6 12 5 7 0 6 5 5z" fill="#ccc"/></svg>Testimonials</li>
      </ul>
    </div>

    <div class="footer-col" style="left:625px">
      <h3>Testimonials</h3>
      <span class="quote-open">&ldquo;</span>
      <p class="footer-note" style="margin-top:24px;margin-left:13px">Olor sit amet conse ctetur adipisicing elit, sed do eiusmod tempor incididunt ut labore et dolore magna aliqua. Ut enim ad minim veniam, quis nostrud exercitation ullamco.</p>
      <div class="signature-row">
        <span class="signature">Mrs. Ivy</span>
        <span class="quote-close">&raquo;</span>
      </div>
    </div>

    <div class="footer-col" style="left:887px">
      <h3>Delivery</h3>
      <p class="footer-note" style="margin-top:24px;width:210px">Olor sit amet conse ctetur adipisicing elit, sed do eiusmod tempor incididunt ut labore et dolore magna aliqua. Ut enim ad minim veniam, quis nostrud exercitation ullamco.</p>
    </div>
  </footer>

  <p class="copyright">&copy; Copyright 2002-2012 Luna Gemcraft Pty Ltd (ABN 12 345 678 901). Luna Gemcraft also trades as Marlow Vane.</p>

</div>
</body>
</html>
```